Artisan Bread Company needs a business card

I need a business card design, for an artisan bread company called "Hollin's Bread".

I would like the logo on one side, and on the other, I would like it to say

Tavish Hollin
Baker
519.362.4175
hollinsbread@mailvexo.com

Not necessarily in that order- but it must have these.

Industry/Entity Type

Business

Font styles to use
Serif

Requirements
Must have
• The provided logo on the front, this on the back-
• Tavish Hollin
• Baker
• 519.362.4175
• hollinsbread@mailvexo.com

```html
<!DOCTYPE html>
<html lang="en">
<head>
<meta charset="utf-8">
<title>Hollin's Bread — Business Card</title>
<link rel="stylesheet" href="https://fonts.googleapis.com/css2?family=Crimson+Text:wght@400;600&display=swap">
<style>
  :root {
    --stage: #2b2b2b;
    --card-dark-top: #4a4a4a;
    --card-dark-bottom: #1f1f1f;
    --card-light-top: #ffffff;
    --card-light-bottom: #d9d9d9;
    --ink: #141414;
    --ink-soft: #4a4a4a;
    --paper: #f4f4f4;
    --rule: #1a1a1a;
    --rule-light: #e8e8e8;
  }
  * { box-sizing: border-box; margin: 0; padding: 0; }
  html, body {
    width: 1200px;
    height: 997px;
    overflow: hidden;
    background: var(--stage);
  }
  .stage {
    width: 1200px;
    height: 997px;
    display: flex;
    flex-direction: column;
    align-items: center;
    justify-content: center;
    gap: 60px;
  }
  .card {
    position: relative;
    width: 740px;
    height: 423px;
    border-radius: 16px;
    overflow: hidden;
    font-family: "Crimson Text", Georgia, serif;
    box-shadow: 0 8px 24px rgba(0,0,0,0.35);
  }
  .card__texture {
    position: absolute;
    inset: 0;
  }
  .card--front .card__texture {
    background: linear-gradient(160deg, var(--card-dark-top), var(--card-dark-bottom));
  }
  .card--back .card__texture {
    background: linear-gradient(160deg, var(--card-light-top), var(--card-light-bottom));
  }

  /* Front: brand mark */
  .brand-front {
    position: absolute;
    inset: 0;
    display: flex;
    flex-direction: column;
    align-items: center;
    justify-content: center;
  }
  .brand-front__name {
    font-size: 72px;
    font-weight: 400;
    color: var(--paper);
    letter-spacing: 1px;
  }
  .brand-front__rule {
    width: 440px;
    height: 2px;
    background: var(--rule-light);
    margin-top: 6px;
  }

  /* Back */
  .brand-back {
    position: absolute;
    left: 55px;
    top: 58px;
  }
  .brand-back__name {
    font-size: 44px;
    font-weight: 400;
    color: var(--ink);
    line-height: 1;
  }
  .brand-back__rule {
    width: 270px;
    height: 2px;
    background: var(--rule);
    margin-top: 12px;
  }
  .person {
    position: absolute;
    right: 55px;
    top: 110px;
    text-align: right;
  }
  .person__name {
    font-size: 34px;
    font-weight: 400;
    color: var(--ink);
    line-height: 1.1;
  }
  .person__role {
    font-size: 15px;
    color: var(--ink-soft);
  }
  .person__rule {
    position: absolute;
    right: 55px;
    top: 178px;
    width: 300px;
    height: 2px;
    background: var(--rule);
  }
  .divider {
    position: absolute;
    left: 55px;
    top: 262px;
    width: 380px;
    height: 2px;
    background: var(--rule);
  }
  .contact {
    position: absolute;
    left: 55px;
    top: 292px;
    list-style: none;
  }
  .contact__item {
    display: flex;
    align-items: center;
    gap: 16px;
    font-size: 22px;
    color: var(--ink);
    margin-bottom: 14px;
  }
  .contact__icon {
    width: 20px;
    height: 20px;
    flex: none;
  }
</style>
</head>
<body>
<main class="stage">

  <section class="card card--front" aria-label="Card front">
    <div class="card__texture" role="img" aria-label="Dark low-poly faceted background texture"></div>
    <div class="brand-front">
      <span class="brand-front__name">Hollin's Bread</span>
      <span class="brand-front__rule"></span>
    </div>
  </section>

  <section class="card card--back" aria-label="Card back">
    <div class="card__texture" role="img" aria-label="Light low-poly faceted background texture"></div>

    <div class="brand-back">
      <div class="brand-back__name">Hollin's Bread</div>
      <div class="brand-back__rule"></div>
    </div>

    <div class="person">
      <div class="person__name">Tavish Hollin</div>
      <div class="person__role">Baker</div>
    </div>
    <div class="person__rule"></div>

    <div class="divider"></div>

    <ul class="contact">
      <li class="contact__item">
        <svg class="contact__icon" viewBox="0 0 24 24" aria-hidden="true">
          <path d="M6.6 10.8a15.1 15.1 0 0 0 6.6 6.6l2.2-2.2a1 1 0 0 1 1-.25 11.4 11.4 0 0 0 3.6.57 1 1 0 0 1 1 1V20a1 1 0 0 1-1 1A17 17 0 0 1 3 4a1 1 0 0 1 1-1h3.5a1 1 0 0 1 1 1c0 1.25.2 2.45.57 3.57a1 1 0 0 1-.25 1z" fill="var(--ink-soft)"/>
        </svg>
        <span>519.362.4175</span>
      </li>
      <li class="contact__item">
        <svg class="contact__icon" viewBox="0 0 24 24" aria-hidden="true">
          <rect x="2" y="5" width="20" height="14" rx="1.5" fill="var(--ink-soft)"/>
          <polyline points="3,6.5 12,13 21,6.5" fill="none" stroke="var(--paper)" stroke-width="1.6"/>
        </svg>
        <span>hollinsbread@mailvexo.com</span>
      </li>
    </ul>
  </section>

</main>
</body>
</html>
```